Tallymint - A/B testing for professionals

We need to improve the presentation layer (design only) of our tool tallymint.example.

www.tallymint.example is a A/B testing tool for websites and all kind of applications. The most important features are already listed on our actual webpage and the attached screenshots.
the animated icons on the front page should be included into the design and should match the color scheme. if you think you need to add a logo or similar things to it - feel free to offer us good proposals. you can reach us by sending us a mail to: support@tallymint.example

our needs listed:
-we'd rather have a very good improvement of the actual design instead of a big redesign with all colours changed etc.
- the pages in the screenshots attached should be redesigned. The amount of different layouts will be around 2 - 4 depending on the design.
- the animated icons on www.tallyrmint.example must be included into the design.
- the colors should match with the animated icons.
- we won't need any code. Psd / ai / graphic files only.

Target Market(s)

everyone who sells something with their webpage / application.

Number of Pages Required

3 page

Colors
85cae6
3276b5
85abd2
cee9f5
eaf1f7
0455a3
000000
0492cd

Requirements
Must have
• - animated icons included on the main page.
• - color match with the animated icons on our website or good proposal for adjusting them accordingly.
• - touch of that is highly scaleable and adjustable: we invented a new query language for the project
• - sweetness of the modern web projects and libraries
• - touch that the date are not shared between different users - high value on privacy
Nice to have
• - proposal for a matching logo or including the actual properly
Should not have
• - images people in the design
• - coded versions

```html
<!DOCTYPE html>
<html lang="en">
<head>
<meta charset="utf-8">
<title>Tallymint – A/B testing made for professionals</title>
<link rel="stylesheet" href="https://fonts.googleapis.com/css2?family=Lato:wght@400;700;900&family=Raleway:wght@300;400&family=Open+Sans:wght@300;400&display=swap">
<style>
:root{
  --hero-deep:#0d4a76;
  --hero-mid:#2f86b8;
  --hero-light:#4fa2cf;
  --subnav:#55a9d3;
  --panel-bg:#ddeef5;
  --brand:#0455a3;
  --brand-bright:#0492cd;
  --sky:#85cae6;
  --ink:#2b2f38;
  --muted:#9aa4ad;
  --body:#6d7680;
  --white:#ffffff;
  --footer:#1e2131;
  --footer-base:#181b29;
  --footer-line:#343849;
  --footer-text:#b9bdc9;
}
*{box-sizing:border-box;margin:0;padding:0}
html,body{width:1200px;height:2612px;overflow:hidden}
body{position:relative;background:var(--white);font-family:"Open Sans",Arial,sans-serif;color:var(--body)}
a{text-decoration:none;color:inherit}

/* hero */
.hero{position:absolute;left:0;top:0;width:1200px;height:563px;
  background:radial-gradient(ellipse 75% 90% at 50% 45%,var(--hero-light) 0%,var(--hero-mid) 45%,var(--hero-deep) 100%);overflow:hidden}
.brand{position:absolute;left:101px;top:24px;font-family:"Lato",sans-serif;font-weight:400;font-size:33px;color:var(--white);letter-spacing:.2px}
.main-nav{position:absolute;right:120px;top:30px;display:flex;align-items:center;gap:0}
.main-nav a{font-family:"Lato",sans-serif;font-size:13px;color:var(--white);margin-left:26px}
.main-nav .login{margin-left:28px;width:98px;height:34px;line-height:34px;text-align:center;background:var(--brand-bright);border-radius:3px;font-weight:700;box-shadow:0 2px 4px rgba(0,0,0,.25)}
.hero-title{position:absolute;left:330px;top:166px;font-family:"Lato",sans-serif;color:var(--white)}
.hero-title h1{font-size:30px;font-weight:700;line-height:1.1}
.hero-title p{font-size:15px;font-weight:400;margin-top:1px}
.btn-install{position:absolute;left:578px;top:178px;width:150px;height:43px;line-height:43px;text-align:center;background:#24282f;color:var(--white);font-family:"Lato",sans-serif;font-size:13px;border-radius:3px}
.btn-more{position:absolute;left:735px;top:178px;width:148px;height:43px;line-height:41px;text-align:center;border:1px solid rgba(255,255,255,.7);color:var(--white);font-family:"Lato",sans-serif;font-size:13px;border-radius:3px}
.hero-shot{position:absolute;left:186px;top:261px;width:812px;height:302px;
  background:linear-gradient(180deg,#e6e8ea 0,#e6e8ea 28px,#ffffff 28px,#f4f6f8 100%);box-shadow:0 0 10px rgba(0,0,0,.25)}
.slide-arrow{position:absolute;top:280px}
.slide-arrow.left{left:22px}
.slide-arrow.right{right:22px}

/* sub navigation */
.sub-nav{position:absolute;left:0;top:563px;width:1200px;height:52px;background:var(--subnav);display:flex;justify-content:center;align-items:center;font-family:"Lato",sans-serif;font-size:13px;color:var(--white)}
.sub-nav .sep{margin:0 26px;opacity:.8}

/* feature cards */
.features{position:absolute;left:0;top:615px;width:1200px;height:688px;background:var(--panel-bg)}
.card{position:absolute;width:316px;height:220px;background:var(--white);text-align:center}
.card.active{background:var(--brand)}
.card .badge{position:absolute;left:50%;top:-31px;margin-left:-31px;width:62px;height:62px;border-radius:50%;background:var(--brand);border:5px solid var(--white);box-shadow:0 1px 4px rgba(0,0,0,.15);display:flex;align-items:center;justify-content:center}
.card.active .badge{background:#0b0e14}
.card h3{margin-top:52px;font-family:"Lato",sans-serif;font-weight:700;font-size:15px;color:var(--ink)}
.card p{margin-top:18px;font-size:11.5px;line-height:20px;color:var(--muted)}
.card .read{display:block;margin-top:24px;font-family:"Lato",sans-serif;font-size:13px;color:var(--brand)}
.card.active h3,.card.active p,.card.active .read{color:var(--white)}

/* stories */
.story-art{position:absolute;border-radius:50%/45%;background:radial-gradient(ellipse at 50% 70%,#a9d9ec 0%,#cfeaf5 45%,rgba(255,255,255,0) 72%)}
.story{position:absolute}
.story h2{font-family:"Raleway",sans-serif;font-weight:300;font-size:28px;color:var(--ink);line-height:1.2}
.story p{margin-top:10px;font-size:13px;line-height:19px;color:var(--body)}
.story .link{color:var(--sky)}
.kbd{display:inline-block;font-family:"Open Sans",sans-serif;font-size:9.5px;padding:0 6px;border:1px solid #cfd4d9;border-radius:3px;background:#f7f8f9;color:var(--ink);line-height:16px}

/* footer */
.rule{position:absolute;left:0;top:2178px;width:1200px;height:8px;background:#eceef0}
.footer{position:absolute;left:0;top:2186px;width:1200px;height:357px;background:var(--footer)}
.f-col{position:absolute;top:87px;width:212px}
.f-col h4{font-family:"Lato",sans-serif;font-weight:900;font-size:15px;letter-spacing:1px;color:var(--white);margin-bottom:14px}
.f-col li{list-style:none;font-size:12px;color:var(--footer-text);height:34px;line-height:33px;border-bottom:1px solid var(--footer-line)}
.f-col li:last-child{border-bottom:none}
.f-col .note{font-size:12px;line-height:19px;color:var(--footer-text)}
.f-input{margin-top:12px;height:30px;line-height:30px;padding-left:16px;background:#25293a;border:1px solid #2f3345;font-size:11.5px;color:var(--footer-text);width:232px}
.f-input + .f-input{margin-top:7px}
.f-btn{margin-top:9px;width:232px;height:30px;line-height:30px;text-align:center;background:var(--brand-bright);color:var(--white);font-family:"Lato",sans-serif;font-weight:900;font-size:11.5px;letter-spacing:1px;border-radius:2px}
.base{position:absolute;left:0;top:2543px;width:1200px;height:69px;background:var(--footer-base);font-size:11px;color:#8d92a0}
.base .copy{position:absolute;left:97px;top:27px}
.base .copy span{margin:0 8px}
.social{position:absolute;right:100px;top:27px;display:flex;gap:14px}
.social i{display:block;width:12px;height:12px;border-radius:50%;background:#565b6b}
</style>
</head>
<body>

<header class="hero">
  <a class="brand" href="#">Tallymint</a>
  <nav class="main-nav">
    <a href="#">Home</a><a href="#">Features</a><a href="#">Install</a><a href="#">Contact</a>
    <a class="login" href="#">LOGIN</a>
  </nav>
  <div class="hero-title">
    <h1>Tallymint</h1>
    <p>A/B testing made for professionals.</p>
  </div>
  <a class="btn-install" href="#">Install &amp; Configure</a>
  <a class="btn-more" href="#">Learn More</a>
  <svg class="slide-arrow left" width="14" height="28" viewBox="0 0 14 28"><polyline points="12,2 2,14 12,26" fill="none" stroke="rgba(255,255,255,.45)" stroke-width="2"/></svg>
  <svg class="slide-arrow right" width="14" height="28" viewBox="0 0 14 28"><polyline points="2,2 12,14 2,26" fill="none" stroke="rgba(255,255,255,.45)" stroke-width="2"/></svg>
  <div class="hero-shot" role="img" aria-label="Screenshot of the browser developer tools showing the page markup and CSS panel"></div>
</header>

<nav class="sub-nav">
  <a href="#">Editor</a><span class="sep">|</span>
  <a href="#">Standard Reports</a><span class="sep">|</span>
  <a href="#">Queries</a><span class="sep">|</span>
  <a href="#">Custom Reports</a>
</nav>

<section class="features">
  <article class="card" style="left:99px;top:113px">
    <div class="badge"><svg width="22" height="22" viewBox="0 0 24 24" fill="none" stroke="#fff" stroke-width="2"><rect x="3" y="5" width="15" height="15" rx="2"/><path d="M10 14l9-9 2 2-9 9h-2z" fill="#fff"/></svg></div>
    <h3>Create Experiments</h3>
    <p>Praesent turpis mauris, aliquet id dolor<br>Gravida adipiscing lectus ut rutrum<br>Aenean at posuere risus.</p>
    <a class="read" href="#">Read More</a>
  </article>
  <article class="card active" style="left:442px;top:113px">
    <div class="badge"><svg width="22" height="22" viewBox="0 0 24 24"><path d="M3 3h9l9 9-9 9-9-9z" fill="#fff"/><circle cx="8" cy="8" r="2" fill="#0b0e14"/></svg></div>
    <h3>Tags</h3>
    <p>Praesent turpis mauris, aliquet id dolor<br>Gravida adipiscing lectus ut rutrum<br>Aenean at posuere risus.</p>
    <a class="read" href="#">Read More</a>
  </article>
  <article class="card" style="left:786px;top:113px">
    <div class="badge"><svg width="24" height="24" viewBox="0 0 24 24"><path d="M1 12s4-7 11-7 11 7 11 7-4 7-11 7S1 12 1 12z" fill="#fff"/><circle cx="12" cy="12" r="3.5" fill="#0455a3"/></svg></div>
    <h3>Preview</h3>
    <p>Praesent turpis mauris, aliquet id dolor<br>Gravida adipiscing lectus ut rutrum<br>Aenean at posuere risus.</p>
    <a class="read" href="#">Read More</a>
  </article>
  <article class="card" style="left:99px;top:387px">
    <div class="badge"><svg width="24" height="24" viewBox="0 0 24 24" fill="none" stroke="#fff" stroke-width="2"><circle cx="12" cy="7" r="4"/><circle cx="7" cy="16" r="4"/><circle cx="17" cy="16" r="4"/></svg></div>
    <h3>Fields</h3>
    <p>Praesent turpis mauris, aliquet id dolor<br>Gravida adipiscing lectus ut rutrum<br>Aenean at posuere risus.</p>
    <a class="read" href="#">Read More</a>
  </article>
  <article class="card" style="left:442px;top:387px">
    <div class="badge"><svg width="20" height="22" viewBox="0 0 20 24" fill="none" stroke="#fff" stroke-width="2"><path d="M3 2h9l5 5v15H3z"/><path d="M6 12h8M6 16h8"/></svg></div>
    <h3>Reports</h3>
    <p>Praesent turpis mauris, aliquet id dolor<br>Gravida adipiscing lectus ut rutrum<br>Aenean at posuere risus.</p>
    <a class="read" href="#">Read More</a>
  </article>
  <article class="card" style="left:786px;top:387px">
    <div class="badge"><svg width="22" height="22" viewBox="0 0 24 24"><path d="M22 2L2 10l8 3 3 8z" fill="#fff"/></svg></div>
    <h3>Queries</h3>
    <p>Praesent turpis mauris, aliquet id dolor<br>Gravida adipiscing lectus ut rutrum<br>Aenean at posuere risus.</p>
    <a class="read" href="#">Read More</a>
  </article>
</section>

<div class="story-art" style="left:148px;top:1385px;width:262px;height:210px" role="img" aria-label="Isometric illustration of an office building on a round light blue base"></div>
<section class="story" style="left:432px;top:1440px;width:600px">
  <h2>Create experiments directly on the website</h2>
  <p>The installation of Tallymint enables a keyboard shortcut <span class="kbd">CTRL + ALT + E</span> on the website. Using this shortcut it is easily possible to create lots of experiments. As long as logged in on Tallymint this shortcut <span class="link">will open the editor</span> and it will assist for special desires.</p>
</section>

<section class="story" style="left:148px;top:1697px;width:612px">
  <h2>Check results with available reports</h2>
  <p>There are <span class="link">quite a few reports available</span> to analyse results. Especially the system wide reports which make use of hashtags are really helpful to find out what the users desire. And even if those system reports are insufficient, Tallymint supports custom reports!</p>
</section>
<div class="story-art" style="left:784px;top:1655px;width:252px;height:192px" role="img" aria-label="Isometric illustration of a large monitor showing a bar chart on a round light blue base"></div>

<div class="story-art" style="left:139px;top:1942px;width:262px;height:175px" role="img" aria-label="Isometric illustration of low buildings on a round light blue base"></div>
<section class="story" style="left:418px;top:1958px;width:612px">
  <h2>Flexible analysis using DQL</h2>
  <p>Tallymint introduces a <span class="link">draw query language (DQL)</span> which is more or less the same as SQL with an output solution. This language is easy to learn, and allows reading the users mind by just painting the data in fancy charts!</p>
</section>

<div class="rule"></div>
<footer class="footer">
  <div class="f-col" style="left:99px">
    <h4>MENU 1</h4>
    <ul><li>Documentation</li><li>Guides</li><li>Query Docs</li><li>Report Docs</li></ul>
  </div>
  <div class="f-col" style="left:355px">
    <h4>MENU 2</h4>
    <ul><li>Information</li><li>Ask Questions</li><li>Answer Questions</li><li>Official Blog</li></ul>
  </div>
  <div class="f-col" style="left:613px">
    <h4>MENU 3</h4>
    <ul><li>About</li><li>Privacy</li><li>Contact</li><li>About us</li></ul>
  </div>
  <div class="f-col" style="left:869px;width:232px">
    <h4>NEWS LETTER</h4>
    <p class="note">Lorem ipsum dolor sit amet, consectetur adipiscing elit.</p>
    <div class="f-input">Name</div>
    <div class="f-input">Email</div>
    <div class="f-btn">SUBSCRIBE</div>
  </div>
</footer>
<div class="base">
  <p class="copy">Copyright 2015 yoursite<span>|</span>All Rights Reserved</p>
  <div class="social"><i></i><i></i><i></i><i></i></div>
</div>

</body>
</html>
```